Buff & Gleam

polished concrete and epoxy coatings flooring company

Target Market(s)

Industrial commercial

Industry/Entity Type

Industrial flooring contractor

Contact Information for Business Card

POLISHED CONCRETE • EPOXY COATING • TERRAZZO RESTORATION • SHOT BLASTING • SURFACE PREPARATION • JOINT FILLING • TILE/ CARPET /GLUE REMOVAL

Colors
0054AA
0677BA
7BADD7
CADEEF
E8F1F8

Requirements
Must have
• email buffandgleamfloors@mailnest.test Address 24593 Wendover Hwy, Fraser, MI 48031. Name Ray Tullin. Services Polished concrete- Epoxy Coatings- Terrazzo restoration-surface preparation- safety striping- joint filling- tile/ carpet/ glue removal phone number 586-555-0173 email buffandgleamfloors.test
Nice to have
• Instagram Facebook logo maybe smaller in the corner

```html
<!DOCTYPE html>
<html lang="en">
<head>
<meta charset="utf-8">
<title>Buff &amp; Gleam — Business Card</title>
<link href="https://fonts.googleapis.com/css2?family=Poppins:wght@400;500;600&display=swap" rel="stylesheet">
<style>
  :root {
    --bg: #082a50;
    --brand-blue: #1176be;
    --deep-blue: #0054aa;
    --light-blue: #7badd7;
    --pale-blue: #cadeef;
    --white: #ffffff;
    --ink: #1a1a1a;
    --silver: #a9adb2;
  }
  * { margin: 0; padding: 0; box-sizing: border-box; }
  html, body { width: 1200px; height: 1200px; overflow: hidden; }
  body {
    background: var(--bg);
    font-family: "Poppins", sans-serif;
    position: relative;
  }
  .card {
    position: absolute;
    left: 230px;
    width: 739px;
    height: 443px;
    overflow: hidden;
  }
  .card--front { top: 132px; background: var(--white); }
  .card--back { top: 625px; }

  .front-panel { position: absolute; inset: 0; }

  .brand-name {
    position: absolute;
    color: var(--white);
    font-weight: 600;
    text-align: center;
    line-height: 1.05;
    letter-spacing: 2px;
  }
  .card--front .brand-name { left: 40px; width: 232px; top: 148px; font-size: 44px; }

  .holder-name {
    position: absolute;
    left: 336px; top: 118px;
    font-size: 35px; font-weight: 600;
    color: var(--brand-blue);
    letter-spacing: 0.5px;
    line-height: 1.1;
  }
  .holder-name::after {
    content: ""; display: block;
    height: 5px; margin-top: 2px;
    background: var(--brand-blue);
    border-radius: 0 3px 3px 0;
  }

  .contact-list { position: absolute; left: 335px; top: 203px; list-style: none; }
  .contact-item {
    display: flex; align-items: center; gap: 7px;
    height: 24px; margin-bottom: 6.5px;
    font-size: 16px; color: var(--ink);
  }
  .contact-icon { width: 24px; height: 24px; flex: none; }

  .back-texture {
    position: absolute; inset: 0;
    background:
      radial-gradient(ellipse 260px 200px at 76% 88%, #13bdf0 0%, rgba(19,189,240,0) 100%),
      linear-gradient(180deg, #1176be 0%, #1177c0 45%, #0f7fcd 100%);
  }
  .service-list { position: absolute; left: 83px; top: 84px; list-style: none; }
  .service-item {
    height: 39.6px;
    font-size: 21px; font-weight: 500;
    color: var(--white);
    display: flex; align-items: center;
  }
  .service-item::before { content: "-"; width: 28px; flex: none; }
  .card--back .brand-name { left: 450px; width: 226px; top: 148px; font-size: 44px; }
</style>
</head>
<body>

<section class="card card--front">
  <svg class="front-panel" viewBox="0 0 739 443" width="739" height="443">
    <defs>
      <linearGradient id="bevel" x1="0" y1="0" x2="0" y2="1">
        <stop offset="0" stop-color="#ffffff"/>
        <stop offset="0.25" stop-color="#8d9196"/>
        <stop offset="0.7" stop-color="#c9ccd0"/>
        <stop offset="1" stop-color="#ffffff"/>
      </linearGradient>
    </defs>
    <path d="M0 0 H122 C236 0 313 84 313 194 V443 H0 Z" fill="url(#bevel)"/>
    <path d="M0 0 H112 C222 0 302 84 302 194 V443 H0 Z" fill="var(--brand-blue)"/>
  </svg>

  <div class="brand-name">BUFF<br>&amp;<br>GLEAM</div>

  <h1 class="holder-name">RAY TULLIN</h1>

  <ul class="contact-list">
    <li class="contact-item">
      <svg class="contact-icon" viewBox="0 0 24 24"><circle cx="12" cy="12" r="12" fill="var(--brand-blue)"/><circle cx="12" cy="10" r="3" fill="none" stroke="#fff" stroke-width="1.6"/><path d="M7 17.5 H17" stroke="#fff" stroke-width="1.6"/><path d="M12 13 V16" stroke="#fff" stroke-width="1.4"/></svg>
      24593 Wendover Hwy, Fraser, MI 48031
    </li>
    <li class="contact-item">
      <svg class="contact-icon" viewBox="0 0 24 24"><circle cx="12" cy="12" r="12" fill="var(--brand-blue)"/><path d="M8.2 6.5 L10 6.3 L11 9.2 L9.8 10.3 C10.6 12 11.9 13.3 13.6 14.1 L14.8 12.9 L17.6 13.9 L17.4 15.7 C16.9 16.6 15.8 17 14.7 16.7 C11.1 15.6 8.3 12.8 7.2 9.2 C6.9 8.1 7.3 7 8.2 6.5 Z" fill="#fff"/></svg>
      586-555-0173
    </li>
    <li class="contact-item">
      <svg class="contact-icon" viewBox="0 0 24 24"><circle cx="12" cy="12" r="12" fill="var(--brand-blue)"/><rect x="6.5" y="8" width="11" height="8" rx="1" fill="#fff"/><path d="M6.8 8.4 L12 12.4 L17.2 8.4" fill="none" stroke="var(--brand-blue)" stroke-width="1"/></svg>
      buffandgleamfloors@mailnest.test
    </li>
    <li class="contact-item">
      <svg class="contact-icon" viewBox="0 0 24 24"><circle cx="12" cy="12" r="12" fill="var(--brand-blue)"/><g fill="none" stroke="#fff" stroke-width="1.1"><circle cx="12" cy="12" r="6"/><ellipse cx="12" cy="12" rx="2.6" ry="6"/><path d="M6 12 H18 M7 9 H17 M7 15 H17"/></g></svg>
      buffandgleamfloors.test
    </li>
  </ul>
</section>

<section class="card card--back">
  <div class="back-texture" role="img" aria-label="Blue-tinted photo of a polished concrete floor surface"></div>
  <ul class="service-list">
    <li class="service-item">POLISHED CONCRETE</li>
    <li class="service-item">EPOXY COATING</li>
    <li class="service-item">TERRAZZO RESTORATION</li>
    <li class="service-item">SHOT BLASTING</li>
    <li class="service-item">SURFACE PREPARATION</li>
    <li class="service-item">JOINT FILLING</li>
    <li class="service-item">TILE/ CARPET /GLUE REMOVAL</li>
  </ul>
  <div class="brand-name">BUFF<br>&amp;<br>GLEAM</div>
</section>

</body>
</html>
```